Youth Sports Banner Ad - 3x5 ft banner special!

We are looking for a full page ad (8.5x11") to advertise our banner services for Youth Sports leagues. The flyers will be handed out to teams and parents in hopes to draw their business to us for team banners.
We want to show our logo, address (4187 Verbena Ln. Paso Robles). Please include that we are offering a youth sports special price on 3x5 ft team banners for $115 (plus tax). The pricing will include 1 layout with up to 2 revisions. We would like the ad to grab the attention of the audience and ask them to "Call, Email or Stop in Today!"

Our info that needs to be on the banner includes:
email: info@markwell47.net
phone: 805-291-6583

We want to really focus on our quick turnaround as we will be producing the banners withing 1-2 business days after artwork approval.
We would like to include the banner samples if possible, and if you see fit, also include that we would like the potential customer to email us their teams name, roster, and colors to help speed up the layout process.

Target Market(s)

Parents of kids playing youth sports. The flyer is meant to increase awareness of our sign shop, while offering a great discount on banners for youth sports banners.

Font styles to use
Sans Serif

Colors

Designer to choose colors to be used in the design.

Requirements
Must have
• Our logo, $115 plus tax banner price, our business information, request to send over all team information including name, roster, and team colors.
Nice to have
• Would like to see color in the ad! If you can tie in the Kelly green from our logo, that would be great.

```html
<!DOCTYPE html>
<html lang="en">
<head>
<meta charset="utf-8">
<title>Youth Sports Team Banner Special</title>
<link href="https://fonts.googleapis.com/css2?family=Anton&family=Open+Sans:wght@600&display=swap" rel="stylesheet">
<style>
  :root {
    --kelly: #1fa84a;
    --kelly-light: #2cb955;
    --kelly-dark: #179a3f;
    --ink: #0d0d0d;
    --paper: #ffffff;
    --paper-shade: #eeeeee;
    --panther-black: #111111;
    --panther-orange: #f08a1c;
    --bandit-purple: #3b3a93;
  }
  * { margin: 0; padding: 0; box-sizing: border-box; }
  html, body { width: 1000px; height: 1200px; overflow: hidden; background: var(--paper); }
  .flyer {
    position: relative; width: 1000px; height: 1200px;
    font-family: "Anton", "Arial Narrow", sans-serif; color: var(--ink);
  }

  /* Header */
  .header { position: relative; height: 212px; background: var(--paper); overflow: hidden; }
  .header .price-wedge { position: absolute; inset: 0; }
  .headline { position: absolute; left: 58px; top: 44px; }
  .headline .title { font-size: 92px; line-height: 1; color: var(--kelly); letter-spacing: 2px; }
  .headline .subtitle { font-size: 31px; line-height: 1; color: var(--kelly); margin-top: 12px; letter-spacing: 0.5px; }
  .price { position: absolute; left: 665px; top: 22px; display: flex; align-items: center; color: var(--paper); }
  .price .for { font-size: 32px; line-height: 1; text-align: center; margin-right: 14px; }
  .price .for .dollar { display: block; font-size: 46px; }
  .price .for .tax { display: block; font-size: 15px; letter-spacing: 0.5px; margin-top: 6px; }
  .price .amount { font-size: 186px; line-height: 1; letter-spacing: -2px; }

  /* Samples band */
  .samples {
    position: relative; height: 353px;
    background: radial-gradient(circle at 50% 40%, var(--kelly-light), var(--kelly-dark));
  }
  .sample { position: absolute; top: 35px; width: 432px; height: 240px; box-shadow: 4px 5px 6px rgba(0,0,0,0.45); }
  .sample-baseball { left: 59px; background: linear-gradient(180deg, var(--panther-black) 0 89%, var(--panther-orange) 89% 100%); }
  .sample-soccer { left: 524px; background: linear-gradient(180deg, var(--bandit-purple) 0 86%, var(--panther-black) 86% 100%); }
  .samples .includes {
    position: absolute; left: 0; right: 0; top: 300px; text-align: center;
    font-size: 34px; line-height: 1; color: var(--paper); letter-spacing: 0.5px;
  }

  /* Call to action */
  .cta { position: relative; height: 367px; background: linear-gradient(90deg, var(--paper-shade), var(--paper) 30%, var(--paper) 70%, var(--paper-shade)); }
  .cta .ask { position: absolute; left: 58px; top: 28px; line-height: 1; }
  .cta .ask .small { font-size: 60px; letter-spacing: 1px; }
  .cta .ask .green { font-size: 132px; color: var(--kelly); margin-top: 2px; }
  .cta .ask .black { font-size: 136px; margin-top: -6px; }
  .brand { position: absolute; left: 640px; top: 70px; width: 300px; font-size: 72px; line-height: 1.05; color: var(--kelly); letter-spacing: 1px; }
  .team-info {
    position: absolute; left: 640px; top: 240px; width: 300px;
    font-family: "Open Sans", Arial, sans-serif; font-weight: 600; font-size: 18px; line-height: 24px; color: var(--ink);
  }

  /* Turnaround strip */
  .turnaround {
    height: 77px; background: var(--kelly); color: var(--paper);
    font-family: "Open Sans", Arial, sans-serif; font-weight: 600; font-size: 27px; line-height: 31px;
    display: flex; align-items: center; justify-content: center; text-align: center;
  }

  /* Contact */
  .contact { height: 191px; text-align: center; padding-top: 26px; }
  .contact .line { font-size: 30px; line-height: 1; letter-spacing: 0.5px; }
  .contact .phone { font-size: 106px; line-height: 1; color: var(--kelly); margin-top: 14px; letter-spacing: 2px; }
</style>
</head>
<body>
<main class="flyer">
  <header class="header">
    <svg class="price-wedge" width="1000" height="212" viewBox="0 0 1000 212" aria-hidden="true">
      <defs>
        <radialGradient id="wedgeGlow" cx="0.8" cy="0.5" r="0.7">
          <stop offset="0" stop-color="#2cb955"/>
          <stop offset="1" stop-color="#179a3f"/>
        </radialGradient>
      </defs>
      <polygon points="678,0 1000,0 1000,212 593,212" fill="url(#wedgeGlow)"/>
    </svg>
    <div class="headline">
      <div class="title">YOUTH SPORTS</div>
      <div class="subtitle">SPECIAL PRICE ON 3X5 FT TEAM BANNERS</div>
    </div>
    <div class="price">
      <div class="for">FOR<span class="dollar">$</span><span class="tax">PLUS TAX</span></div>
      <div class="amount">115</div>
    </div>
  </header>

  <section class="samples">
    <div class="sample sample-baseball" role="img" aria-label="Sample baseball team banner with panther mascot, team name, player roster, coaches and sponsor"></div>
    <div class="sample sample-soccer" role="img" aria-label="Sample soccer team banner with bandit mascot and soccer ball, numbered player roster, head coach and sponsor"></div>
    <p class="includes">PRICING INCLUDES 1 CUSTOM LAYOUT WITH UP TO 2 REVISIONS</p>
  </section>

  <section class="cta">
    <div class="ask">
      <div class="small">CALL, EMAIL OR</div>
      <div class="green">STOP IN</div>
      <div class="black">TODAY!</div>
    </div>
    <div class="brand">MARKWELL<br>SIGNS</div>
    <p class="team-info">Email us your team name, roster and team colors to speed up your layout!</p>
  </section>

  <p class="turnaround">All orders will be finished within 1-2 days following<br>final artwork approval</p>

  <footer class="contact">
    <div class="line">4187 VERBENA LN. PASO ROBLES &nbsp;|&nbsp; EMAIL: INFO@MARKWELL47.NET</div>
    <div class="phone">PH: 805-291-6583</div>
  </footer>
</main>
</body>
</html>
```